BrawnCrate placard

I need a placard designed that will go in my monthly subscription boxes to describe the products inside. There must be space to write 3-5 sentences on each product.
the first area will be titled: For your flowing mane
2 for your macho glow
3 to keep you smelling macho
4 to keep you clanging and banging at the gym.
Placard will be 5inchs wide and 7inchs long

I have attached the logo and the website address must be used in the design brawncrates.com.

Target Market(s)

men between 20-50

Colors

Designer to choose colors to be used in the design.

Requirements
Must have
• My website address brawncrates.com
• 4 area to write 3-5 sentences
• 1 for your flowing mane
• 2to keep you smelling macho
• 3 to keep you clanging and banging at the gym
• 4 for your macho glow

```html
<!DOCTYPE html>
<html lang="en">
<head>
<meta charset="utf-8">
<title>BrawnCrate Placard</title>
<link rel="stylesheet" href="https://fonts.googleapis.com/css2?family=Oswald:wght@600;700&family=Lato:ital,wght@0,400;0,700;1,700&display=swap">
<style>
  :root {
    --red: #ec1c24;
    --black: #0d0d0d;
    --grey: #555555;
    --ink: #222222;
    --white: #ffffff;
    --canvas: #f3f3f3;
  }
  * { margin: 0; padding: 0; box-sizing: border-box; }
  html, body { width: 1200px; height: 1200px; overflow: hidden; background: var(--canvas); }
  .placard {
    position: absolute; left: 238px; top: 93px;
    width: 846px; height: 1184px;
    transform: scale(0.856); transform-origin: 0 0;
    background: var(--white); overflow: hidden;
    font-family: "Lato", sans-serif; color: var(--ink);
  }
  .shapes { position: absolute; inset: 0; }
  .headline {
    position: absolute; left: 364px; top: 70px;
    font-family: "Oswald", sans-serif; font-weight: 700;
    font-size: 33px; line-height: 37px; letter-spacing: 1.2px;
    color: var(--white); text-transform: uppercase;
  }
  .brand { position: absolute; left: 20px; top: 252px; width: 290px; }
  .brand-name {
    font-family: "Lato", sans-serif; font-weight: 700;
    font-size: 37px; letter-spacing: 1px; color: var(--black);
    display: flex; align-items: center; gap: 10px;
  }
  .brand-mark { width: 22px; height: 22px; background: var(--red); }
  .brand-tagline {
    margin-top: 8px; font-family: "Oswald", sans-serif; font-weight: 600;
    font-size: 10.5px; letter-spacing: -0.2px; color: var(--black); text-transform: uppercase;
  }
  .item { position: absolute; }
  .item-tab {
    position: absolute; background: var(--black); color: var(--white);
    font-family: "Lato", sans-serif; font-style: italic; font-weight: 700;
    font-size: 22px; line-height: 28px; padding-left: 12px;
    display: flex; align-items: center;
    clip-path: polygon(0 0, 96% 0, 100% 100%, 0 100%);
  }
  .item-number {
    position: absolute; width: 76px; height: 76px; border-radius: 50%;
    border: 3px solid var(--red); background: var(--white);
    display: flex; align-items: center; justify-content: center;
    font-family: "Oswald", sans-serif; font-weight: 700; font-size: 46px; color: var(--black);
  }
  .item-body { position: absolute; font-size: 21px; line-height: 26.7px; color: var(--ink); }
  .justify { text-align: justify; hyphens: manual; }
  .site {
    position: absolute; left: 63px; top: 1146px;
    color: var(--white); font-size: 20px; letter-spacing: 2.2px;
  }
</style>
</head>
<body>
  <main class="placard">
    <svg class="shapes" width="846" height="1184" viewBox="0 0 846 1184" aria-hidden="false">
      <defs>
        <linearGradient id="photoTone" x1="0" y1="0" x2="1" y2="1">
          <stop offset="0" stop-color="#b9b6b1"/>
          <stop offset="0.5" stop-color="#6c6c6e"/>
          <stop offset="1" stop-color="#2e2f33"/>
        </linearGradient>
      </defs>
      <polygon points="570,0 622,0 597,31 545,31" fill="var(--red)"/>
      <polygon points="370,31 846,31 846,187 245,187" fill="var(--black)"/>
      <polygon points="245,187 470,187 370,262" fill="var(--grey)"/>
      <polygon points="470,187 846,187 846,874 270,373" fill="var(--red)"/>
      <polygon points="505,187 846,187 846,846 318,372" fill="url(#photoTone)" role="img" aria-label="Photo of a well-groomed man in a grey wool coat standing on a city street"/>
      <polygon points="0,1100 820,1184 0,1184" fill="var(--red)"/>
    </svg>

    <h1 class="headline">Men's Grooming &amp; Essentials<br>For The Everyday Macho</h1>

    <div class="brand">
      <div class="brand-name"><span class="brand-mark"></span>BRAWNCRATE</div>
      <p class="brand-tagline">Mens grooming and essentials for the everyday macho man</p>
    </div>

    <section class="item">
      <div class="item-tab" style="left:100px;top:471px;width:255px;height:33px;padding-left:20px;">for your flowing mane</div>
      <div class="item-number" style="left:33px;top:450px;">1</div>
      <p class="item-body" style="left:42px;top:532px;width:420px;">Lorem Ipsum is simply dummy text of the printing and typesetting industry. Lorem Ipsum has been the industry's standard dummy text ever since</p>
    </section>

    <section class="item">
      <div class="item-tab" style="left:100px;top:677px;width:317px;height:33px;padding-left:26px;">to keep you smelling macho</div>
      <div class="item-number" style="left:33px;top:656px;">2</div>
      <p class="item-body justify" style="left:46px;top:744px;width:616px;">Lorem Ipsum is simply dummy text of the printing and typeset-ting industry. Lorem Ipsum has been the industry's standard dummy text ever since</p>
    </section>

    <section class="item">
      <div class="item-tab" style="left:95px;top:879px;width:328px;height:62px;padding-left:33px;">to keep you clanging and<br>banging at the gym</div>
      <div class="item-number" style="left:33px;top:871px;">3</div>
      <p class="item-body justify" style="left:50px;top:957px;width:340px;">Lorem Ipsum is simply dummy text of the printing and typesetting in-dustry. Lorem Ipsum has been the industry's standard dummy text ever since</p>
    </section>

    <section class="item">
      <div class="item-tab" style="left:530px;top:889px;width:255px;height:38px;padding-left:20px;">for your macho glow</div>
      <div class="item-number" style="left:462px;top:868px;">4</div>
      <p class="item-body justify" style="left:483px;top:949px;width:282px;">Lorem Ipsum is simply dummy text of the printing and typesetting industry. Lorem Ipsum has been the in-dustry's standard dummy text ever since</p>
    </section>

    <p class="site">www.brawncrates.com</p>
  </main>
</body>
</html>
```